Letterhead Design for Corvane Communications

We are a Telecommunications Company, We wanting to get our Letterhead sorted as the one we have now looks Dull, It be used across our different databases we use but also mainly in Word , I have attached our Logo for you also, our website is corvane-example.com.au

We would only like to show our postal Address which is PO Box 8142 Tilford Cove NSW 2497

and we need to show our ABN Number Which we would be ABN: 61 804 327 918

Target Market(s)

Looks Stunning for our Proposals and General Usage

Industry/Entity Type

Telecommunications

Requirements
Must have
• Our Postal Address Only and Our ABN Number
Should not have
• Not listing our Actual Address

```html
<!DOCTYPE html>
<html lang="en">
<head>
<meta charset="utf-8">
<title>Corvane Communications Letterhead</title>
<link rel="stylesheet" href="https://fonts.googleapis.com/css2?family=Montserrat:wght@400;700&family=Open+Sans:wght@400&display=swap">
<style>
  :root {
    --backdrop: #e2e3e4;
    --paper: #ffffff;
    --brand-orange: #d15a27;
    --brand-green: #1f9a45;
    --ink: #2b2b2b;
    --footer-text: #ffffff;
  }
  * { box-sizing: border-box; margin: 0; padding: 0; }
  html, body {
    width: 1200px; height: 1200px; overflow: hidden;
    background: var(--backdrop);
  }
  .letterhead {
    position: absolute; left: 197px; top: 30px;
    width: 806px; height: 1140px;
    background: var(--paper);
    box-shadow: 0 6px 24px rgba(0,0,0,0.12);
    font-family: "Open Sans", Arial, sans-serif;
    color: var(--ink);
  }
  .brand {
    position: absolute; left: 70px; top: 62px;
    display: flex; align-items: center; gap: 16px;
  }
  .brand-dot {
    width: 64px; height: 64px; border-radius: 50%;
    background: var(--brand-orange);
  }
  .brand-name {
    font-family: "Montserrat", Arial, sans-serif;
    font-weight: 700; font-size: 30px; letter-spacing: 2px;
    color: var(--brand-orange); text-transform: uppercase;
  }
  .recipient {
    position: absolute; left: 70px; top: 300px;
    font-size: 14px; line-height: 1.45;
  }
  .salutation {
    position: absolute; left: 70px; top: 415px; font-size: 14px;
  }
  .body-copy {
    position: absolute; left: 70px; top: 455px; width: 666px;
    font-size: 14px; line-height: 1.6;
  }
  .closing {
    position: absolute; left: 70px; top: 790px; font-size: 14px;
  }
  .signature {
    position: absolute; left: 90px; top: 825px;
    width: 300px; height: 90px;
    background: linear-gradient(90deg, #f4f4f4, #fafafa);
  }
  .footer {
    position: absolute; left: 0; bottom: 0; width: 100%; height: 100px;
    background: var(--brand-orange);
    border-top: 4px solid var(--brand-green);
    box-shadow: 0 -4px 0 var(--paper);
    color: var(--footer-text);
    font-family: "Montserrat", Arial, sans-serif; font-size: 13px;
    display: flex; flex-direction: column; align-items: center; justify-content: center;
    gap: 6px;
  }
  .footer-row { display: flex; align-items: center; gap: 8px; }
  .footer-sep { opacity: 0.9; }
  .footer-icon { width: 11px; height: 11px; fill: var(--footer-text); }
</style>
</head>
<body>
  <div class="letterhead">
    <header class="brand">
      <div class="brand-dot"></div>
      <div class="brand-name">Corvane Communications</div>
    </header>

    <address class="recipient" style="font-style:normal">
      Mr. Elliot Marsh<br>
      President<br>
      Harbourline Accountants<br>
      48 Kellaway Road,<br>
      Marlow Heights NSW 2560
    </address>

    <p class="salutation">Dear :</p>

    <p class="body-copy">Lorem ipsum dolor sit amet, consectetur adipiscing elit. Aenean ut ipsum eget massa hendrerit vestibulum vel in velit. Donec pretium neque velit. Aliquam porta lectus nec mauris ornare venenatis. Vivamus non est turpis, et cursus sem. Mauris vehicula erat in diam auctor at bibendum nisl lacinia. Morbi imperdiet neque vehicula nunc convallis gravida. Vestibulum iaculis pretium placerat. Integer consequat, est sit amet facilisis eleifend, nibh nibh varius orci, eget dapibus arcu dui non purus. Pellentesque in magna mauris. Duis enim sapien, dictum vitae condimentum a, pulvinar vel lacus. Mauris et molestie nibh. Vestibulum vitae nulla at metus elementum porta sit amet interdum elit. Nulla sollicitudin neque eu nulla volutpat congue. Etiam pellentesque, velit id dapibus fermentum, turpis sapien ornare dui, ac tincidunt ligula odio congue purus. Nunc sed ante dui, in porta lectus. Cras nec sem lorem. In hac habitasse platea dictumst. Maecenas id diam quis dui porta tristique. Sed id egestas felis. Donec ullamcorper mattis posuere. Phasellus fermentum eleifend tortor vel dapibus. Vestibulum ante ipsum.</p>

    <p class="closing">Sincerely,</p>
    <div class="signature" role="img" aria-label="Handwritten signature of Nathaniel Reyes"></div>

    <footer class="footer">
      <div class="footer-row">PO Box 8142 Tilford Cove NSW 2497 <span class="footer-sep">|</span> ABN: 61 804 327 918</div>
      <div class="footer-row">
        <svg class="footer-icon" viewBox="0 0 24 24"><path d="M6.6 10.8a15.1 15.1 0 0 0 6.6 6.6l2.2-2.2c.3-.3.7-.4 1-.2 1.1.4 2.3.6 3.6.6.6 0 1 .4 1 1V20c0 .6-.4 1-1 1A17 17 0 0 1 3 4c0-.6.4-1 1-1h3.5c.6 0 1 .4 1 1 0 1.3.2 2.5.6 3.6.1.3 0 .7-.2 1z"/></svg>
        02 5550 1847 <span class="footer-sep">|</span>
        <svg class="footer-icon" viewBox="0 0 24 24"><path d="M2 5h20v14H2zm2 2v.5l8 5 8-5V7H4zm0 3v7h16v-7l-8 5z"/></svg>
        nathaniel.reyes@corvane-example.com.au <span class="footer-sep">|</span>
        <svg class="footer-icon" viewBox="0 0 24 24"><circle cx="12" cy="12" r="9" fill="none" stroke="#fff" stroke-width="2"/><path d="M3 12h18M12 3c3 3 3 15 0 18M12 3c-3 3-3 15 0 18" fill="none" stroke="#fff" stroke-width="1.6"/></svg>
        www.corvane-example.com.au
      </div>
    </footer>
  </div>
</body>
</html>
```